Hollow Bluff Cellars Reserve Cabernet Sauvignon Wine Labels front and back

I need a front and back wine label. For a new RESERVE Cabernet Sauvignon wine. I am attaching the details and some ideas and possible images to use. But creativity is encouraged. This wine will be seen on wine shop and grocery store shelves so it needs to pop while appearing elegant and to be about $50/bottle of wine. The front and back labels should go together nicely. I would like some foil on the front, but not the back. We are trying to show the natural beauty of our vineyards and the elegance of our wines. We would like to invoke a feel of sustainability, proudly family owned and operated.

Target Market(s)

21-50 year olds, red wine drinkers, higher priced wine drinkers

Industry/Entity Type

Wine

Font styles to use
Serif
Script

Colors

Designer to choose only greyscale colors for use in the design.

Requirements
Must have
• Front Label with specified details and Back label with specified details. Foil banner on the front label that says " Family stewards of the land for 5 generations"the front label that says
Nice to have
• vineyard or winery background, have include a sample or example, some gold or bronze or silver accents

```html
<!DOCTYPE html>
<html lang="en">
<head>
<meta charset="utf-8">
<title>Hollow Bluff Cellars Reserve Cabernet Sauvignon</title>
<link href="https://fonts.googleapis.com/css2?family=Cinzel:wght@400&family=Pinyon+Script&family=Tinos:wght@400;700&display=swap" rel="stylesheet">
<style>
  :root {
    --label-brown: #4d3f38;
    --vineyard-dark: #261d19;
    --vineyard-mid: #3a2e28;
    --ink-white: #ffffff;
    --gold-deep: #a9761f;
    --gold-mid: #d8aa4c;
    --gold-light: #f6e6c0;
    --banner-text: #3a2a22;
  }
  * { margin: 0; padding: 0; box-sizing: border-box; }
  html, body {
    width: 781px;
    height: 1200px;
    overflow: hidden;
    background: var(--label-brown);
  }
  .label {
    position: relative;
    width: 781px;
    height: 1200px;
    background: var(--label-brown);
    overflow: hidden;
  }
  .vineyard-scene {
    position: absolute;
    left: 0;
    top: 700px;
    width: 781px;
    height: 446px;
    background:
      radial-gradient(ellipse 30% 55% at 50% 38%, rgba(77,63,56,0.85) 0%, rgba(77,63,56,0) 100%),
      linear-gradient(90deg, var(--vineyard-dark) 0%, rgba(38,29,25,0.8) 18%, rgba(58,46,40,0.25) 36%, rgba(58,46,40,0.25) 64%, rgba(38,29,25,0.8) 82%, var(--vineyard-dark) 100%),
      linear-gradient(180deg, rgba(77,63,56,0) 0%, var(--vineyard-mid) 30%, var(--vineyard-dark) 100%);
  }
  .maker-mark {
    position: absolute;
    top: 136px;
    left: 0;
    width: 100%;
    display: flex;
    justify-content: center;
    align-items: center;
    gap: 10px;
  }
  .maker-mark__square {
    width: 16px;
    height: 16px;
    background: var(--gold-mid);
  }
  .maker-mark__name {
    font-family: "Cinzel", serif;
    font-size: 22px;
    color: var(--gold-mid);
    letter-spacing: 2px;
  }
  .winery-name {
    position: absolute;
    top: 232px;
    left: 0;
    width: 100%;
    text-align: center;
    font-family: "Cinzel", serif;
    font-weight: 400;
    color: var(--ink-white);
    line-height: 1;
  }
  .winery-name__main {
    display: block;
    font-size: 70px;
    letter-spacing: 1px;
  }
  .winery-name__sub {
    display: block;
    margin-top: 10px;
    font-size: 70px;
    letter-spacing: 1px;
  }
  .reserve {
    position: absolute;
    top: 418px;
    left: 0;
    width: 100%;
    text-align: center;
    font-family: "Pinyon Script", cursive;
    font-size: 156px;
    line-height: 1.1;
    background: linear-gradient(100deg, var(--gold-deep) 0%, var(--gold-mid) 35%, var(--gold-light) 55%, var(--gold-mid) 75%, var(--gold-deep) 100%);
    -webkit-background-clip: text;
    background-clip: text;
    color: transparent;
  }
  .varietal {
    position: absolute;
    top: 584px;
    left: 0;
    width: 100%;
    text-align: center;
    font-family: "Tinos", serif;
    font-weight: 700;
    font-size: 31px;
    letter-spacing: 1.5px;
    color: var(--ink-white);
  }
  .appellation {
    position: absolute;
    top: 623px;
    left: 0;
    width: 100%;
    text-align: center;
    font-family: "Tinos", serif;
    font-weight: 400;
    font-size: 27px;
    letter-spacing: 0.5px;
    color: var(--ink-white);
  }
  .vintage {
    position: absolute;
    top: 732px;
    left: 0;
    width: 100%;
    text-align: center;
    font-family: "Tinos", serif;
    font-size: 72px;
    line-height: 1;
    background: linear-gradient(100deg, var(--gold-deep) 0%, var(--gold-mid) 45%, var(--gold-light) 60%, var(--gold-deep) 100%);
    -webkit-background-clip: text;
    background-clip: text;
    color: transparent;
  }
  .foil-banner {
    position: absolute;
    left: 0;
    top: 1146px;
    width: 781px;
    height: 54px;
    display: flex;
    align-items: center;
    justify-content: center;
    background: linear-gradient(90deg, var(--gold-deep) 0%, var(--gold-mid) 30%, var(--gold-light) 55%, var(--gold-mid) 78%, var(--gold-deep) 100%);
  }
  .foil-banner__text {
    font-family: "Tinos", serif;
    font-weight: 700;
    font-size: 23px;
    letter-spacing: 0.8px;
    color: var(--banner-text);
    white-space: nowrap;
  }
</style>
</head>
<body>
  <main class="label">
    <div class="vineyard-scene" role="img" aria-label="Engraved vineyard rows and trees framing a barn in rolling hills"></div>

    <div class="maker-mark">
      <span class="maker-mark__square"></span>
      <span class="maker-mark__name">Hollow Bluff Cellars</span>
    </div>

    <h1 class="winery-name">
      <span class="winery-name__main">HOLLOW BLUFF</span>
      <span class="winery-name__sub">- CELLARS -</span>
    </h1>

    <p class="reserve">Reserve</p>
    <p class="varietal">CABERNET SAUVIGNON</p>
    <p class="appellation">HORSE HEAVEN HILLS</p>

    <p class="vintage">2022</p>

    <footer class="foil-banner">
      <span class="foil-banner__text">FAMILY STEWARDS OF THE LAND FOR 5 GENERATIONS</span>
    </footer>
  </main>
</body>
</html>
```